Artificial intelligence company needs a webpage for its datasets

Who are we?

We are a company specializing in AI at the edge, i.e on microcontroller.
We enable developers to create AI library automatically, without any knowledge in machine learning or data science.

Speaking of data, we are developing and soon releasing a portal to show the world our datasets and prototypes, and report on the performances of your product with this data.

What do we need?

We will need from you to design the page showcasing one dataset.
We need it to be easy to understand.
It should be modern and clear.
It should give a feeling of trust into the product and the analysis.
You should maybe think about it as a product page for the data.

Content

It must contains:

- a visual (image or logo) related to the data.
It should quickly give an idea about the content of the dataset.

- a title

- a description.
It will probably spans a few lines and explains what is in the dataset and
how we gathered it.

- a metadata section.
Those are integers summarizing the dataset.
It must include the following info:
. a number of classes ( between 2 and 64)
. a number of columns (between 2 and 4096)
. a number of outliers (up to a few tens of thousands)
. a number of nominal samples (up to a few tens of thousands)

- a performance section
A very important section, it tells the user if he will get good results or not

. balanced accuracy (between 0 and 1)
. confidence (between 0 and 1)
. ram (between 1 and 64 K)

You can represent this data in different ways if you wish., graph, progress bar etc

- a download button for the user to get the data.

Nice to have:

- a section for a few small graphs.
- a section called source containing a link and one called citation with a few line of text, as some datasets will need it.
- a hardware info section
- a simple header and footer

Constraint

We would like you to use as much as possible components available in the Vuetify framework.

Color scheme should be the same or go well with our website www.lunavoltix.example

Inspiration

We like the results found when you search for user persona on Dribbble. Maybe draws inspiration from it. We included a few screenshots.

We also included a screenshot of a prototype we have.

Target Market(s)

Embedded developpers or their managers

Coding

Coded - Design and coding required

Number of Pages Required

1 page

Requirements
Must have
• Title, description, metadata, performance sections
Image in relation with the dataset
Download button
Nice to have
• If the design could also work with a variable number of sections that would be great.
For example, some dataset will need a source and citation section.
And in the future, we will maybe add some small graphs or hardware info section.

```html
<!DOCTYPE html>
<html lang="en">
<head>
<meta charset="utf-8">
<title>Dataset · Ukulele</title>
<link href="https://fonts.googleapis.com/css2?family=Roboto:wght@400;500;700&display=swap" rel="stylesheet">
<style>
:root{
  --ink:#333;
  --muted:#666;
  --soft:#757575;
  --page:#eeeeee;
  --card:#ffffff;
  --pink:#e84a8a;
  --blue:#2979ff;
  --amber:#fbc02d;
  --track:#bdbdbd;
}
*{box-sizing:border-box;margin:0;padding:0}
html,body{width:1042px;height:1200px;overflow:hidden}
body{position:relative;background:var(--page);font-family:'Roboto',Arial,sans-serif;color:var(--ink)}
.app-bar{position:absolute;left:0;top:0;width:1042px;height:49px;background:#fff;box-shadow:0 1px 3px rgba(0,0,0,.12);z-index:3}
.brand{position:absolute;left:62px;top:16px;font-size:14px;font-weight:700;letter-spacing:.6px;color:#333}
.nav a{position:absolute;top:18px;font-size:11px;color:var(--muted);text-decoration:none}
.nav .active{color:#444}
.nav-indicator{position:absolute;left:632px;top:47px;width:66px;height:2px;background:var(--pink)}
.menu-btn{position:absolute;left:987px;top:13px;width:24px;height:24px;border-radius:50%;background:var(--pink)}
.hero{position:absolute;left:0;top:49px;width:1042px;height:322px;
  background:linear-gradient(90deg,#efe2c8 0%,#f6f3ee 14%,#f8f8f8 40%,#f8f8f8 75%,#f4ece2 88%,#efe0cc 100%)}
.card{position:absolute;background:var(--card);box-shadow:0 1px 3px rgba(0,0,0,.12)}
.profile{left:158px;top:139px;width:726px;height:307px}
.avatar{position:absolute;left:67px;top:35px;width:178px;height:178px;border-radius:50%;
  background:radial-gradient(circle at 50% 60%,#b46f3c 0%,#a0522d 35%,#b3262e 70%,#c2303a 100%)}
.avatar-add{position:absolute;left:62px;top:62px;width:54px;height:54px;border-radius:50%;background:rgba(255,255,255,.55)}
.actions{position:absolute;left:128px;top:224px}
.title{position:absolute;left:315px;top:44px;font-size:31px;font-weight:400;color:#333}
.tags{position:absolute;left:315px;top:86px;font-size:12px;font-weight:500;color:var(--soft)}
.aspirations{position:absolute;left:315px;top:119px;font-size:12.5px;font-weight:500;color:#555}
.quote{position:absolute;left:315px;top:139px;font-size:11px;color:var(--muted)}
.lede{position:absolute;left:315px;top:174px;font-size:11px;color:var(--muted)}
.download{position:absolute;left:315px;top:213px;width:90px;height:31px;background:var(--blue);color:#fff;border:0;border-radius:2px;
  font:500 11px 'Roboto',Arial,sans-serif;letter-spacing:.3px;box-shadow:0 2px 3px rgba(0,0,0,.2)}
.section-title{position:absolute;font-size:18px;font-weight:400;color:#333}
.panel{width:352px}
.row{position:absolute;left:20px;font-size:11px;color:var(--muted)}
.row b{font-weight:700}
.slider{position:absolute;left:20px;width:313px;height:2px;background:var(--track)}
.slider i{position:absolute;left:0;top:0;height:2px}
.slider s{position:absolute;top:-4px;width:10px;height:10px;border-radius:50%;margin-left:-5px}
.blue i,.blue s{background:var(--blue)}
.pink i,.pink s{background:var(--pink)}
.amber i,.amber s{background:var(--amber)}
.stat{position:absolute;left:20px;font-size:11px;color:var(--muted)}
.stat b{font-weight:700}
.desc{position:absolute;left:20px;top:37px;width:310px;font-size:11px;line-height:19px;font-weight:500;color:#666}
.stamp{position:absolute;left:20px;top:82px;font-size:10.5px;color:var(--muted)}
.footer-title{position:absolute;left:0;width:1042px;top:1074px;text-align:center;font-size:14px;color:#333}
.copyright{position:absolute;left:0;width:1042px;top:1105px;text-align:center;font-size:11px;color:var(--soft)}
</style>
</head>
<body>
<header class="app-bar">
  <div class="brand">DATASET</div>
  <nav class="nav">
    <a class="active" href="#" style="left:643px">Products</a>
    <a href="#" style="left:710px">Stuff</a>
    <a href="#" style="left:756px">And</a>
    <a href="#" style="left:799px">Things</a>
    <a href="#" style="left:854px">Go</a>
    <a href="#" style="left:891px">Here</a>
    <a href="#" style="left:937px">Contact</a>
  </nav>
  <div class="nav-indicator"></div>
  <div class="menu-btn">
    <svg width="24" height="24" viewBox="0 0 24 24"><g fill="#222"><circle cx="12" cy="7" r="1.6"/><circle cx="12" cy="12" r="1.6"/><circle cx="12" cy="17" r="1.6"/></g></svg>
  </div>
</header>

<div class="hero" role="img" aria-label="Banner photo of an acoustic guitar on the left and hands holding crossed drumsticks on the right"></div>

<section class="card profile">
  <div class="avatar" role="img" aria-label="Round photo of a ukulele lying on red patterned fabric">
    <div class="avatar-add">
      <svg width="54" height="54" viewBox="0 0 54 54"><path d="M27 13v28M13 27h28" stroke="#111" stroke-width="3"/></svg>
    </div>
  </div>
  <div class="actions">
    <svg width="60" height="26" viewBox="0 0 60 26">
      <circle cx="12" cy="13" r="12" fill="var(--pink)"/>
      <path d="M12 19l-5.2-5.1a3.2 3.2 0 0 1 5.2-3.8a3.2 3.2 0 0 1 5.2 3.8z" fill="#fff"/>
      <circle cx="44" cy="13" r="12" fill="var(--pink)"/>
      <g fill="#fff"><circle cx="48" cy="8.5" r="2.3"/><circle cx="39.5" cy="13" r="2.3"/><circle cx="48" cy="17.5" r="2.3"/></g>
      <path d="M48 8.5L39.5 13L48 17.5" stroke="#fff" stroke-width="1.4" fill="none"/>
    </svg>
  </div>
  <h1 class="title">Ukulele</h1>
  <div class="tags">TIME SERIES . VIBRATION</div>
  <div class="aspirations">Aspirations</div>
  <p class="quote">"Bring happiness one chord at a time"</p>
  <p class="lede">Lorem ipsum ipsum ipsum ipsum ipsum ipsum.</p>
  <button class="download">DOWNLOAD</button>
</section>

<h2 class="section-title" style="left:158px;top:502px">METADATA</h2>
<h2 class="section-title" style="left:533px;top:502px">HARDWARE INFO</h2>

<section class="card panel" style="left:158px;top:550px;height:213px">
  <div class="row" style="top:35px">Number of Nominal: <b>256</b></div>
  <div class="slider blue" style="top:59px"><i style="width:24%"></i><s style="left:24%"></s></div>
  <div class="row" style="top:83px">Number of Anomaly: <b>100</b></div>
  <div class="slider pink" style="top:107px"><i style="width:8%"></i><s style="left:8%"></s></div>
  <div class="row" style="top:131px">Number of Samples: <b>1024</b></div>
  <div class="slider amber" style="top:154px"><i style="width:98%"></i><s style="left:98%"></s></div>
</section>

<section class="card panel" style="left:533px;top:550px;height:213px">
  <div class="row" style="top:35px">MCU: <b>LVX-32</b></div>
  <div class="row" style="top:83px">Data Rate: <b>42</b></div>
  <div class="slider pink" style="top:107px"><i style="width:40%"></i><s style="left:40%"></s></div>
  <div class="row" style="top:131px">Range: <b>42</b></div>
  <div class="slider amber" style="top:154px"><i style="width:40%"></i><s style="left:40%"></s></div>
</section>

<h2 class="section-title" style="left:158px;top:819px">PERFORMANCES</h2>
<h2 class="section-title" style="left:533px;top:819px">DESCRIPTION</h2>

<section class="card panel" style="left:158px;top:867px;height:151px">
  <div class="stat" style="top:38px">Balanced Accuracy: <b>0.95</b></div>
  <div class="stat" style="top:58px">Confidence: <b>0.9</b></div>
  <div class="stat" style="top:77px">Ram: <b>4k</b></div>
</section>

<section class="card panel" style="left:533px;top:867px;height:148px">
  <p class="desc">We learned to recognize a few chords as normal and other chords (or no chords at all) as anomaly.</p>
  <div class="stamp">06/15/2020 00:08:34</div>
</section>

<footer>
  <div class="footer-title">Add A Footer</div>
  <div class="copyright">© 2020. DATASET. ALL RIGHTS RESERVED</div>
</footer>
</body>
</html>
```